R.L. Penrose Electric Holiday Party Invitation

We need a cohesive, on-brand holiday party invitation suite for R.L. Penrose Electrical Contractors (slogan Driven by Excellence). Design should include: 1) 5x7" invitation (print + digital), 2) matching RSVP card, and 3) raffle ticket.
Use our brand colors (navy, red, white, light gray) and modern professional style with subtle holiday accents.
Event: Thursday, Dec 18 2025 | 6-10 PM | Ravenna Bellhaven, 318 Quillby Ave, Hammonton NJ 08037.
RSVP by: Dec 1 | Plus one allowed.
Deliver print-ready PDFs + editable source files.

```html
<!DOCTYPE html>
<html lang="en">
<head>
<meta charset="utf-8">
<title>R.L. Penrose Electric Holiday Party Invitation Suite</title>
<link rel="stylesheet" href="https://fonts.googleapis.com/css2?family=Cinzel:wght@700&family=Open+Sans:wght@400;600;700&family=PT+Serif:wght@700&family=Arimo:wght@400;700&display=swap">
<style>
  :root {
    --page: #ffffff;
    --navy-deep: #141c5a;
    --navy: #1b2a80;
    --blue-glow: #2f7fe0;
    --red-glow: #e2405e;
    --red: #d8263a;
    --white: #ffffff;
    --light-gray: #d9dce6;
    --gold-line: #d8c9a0;
  }
  * { margin: 0; padding: 0; box-sizing: border-box; }
  html, body { width: 1200px; height: 1200px; overflow: hidden; background: var(--page); }
  .canvas { position: relative; width: 1200px; height: 1200px; }

  /* Invitation card */
  .invitation {
    position: absolute; left: 25px; top: 186px; width: 592px; height: 828px; overflow: hidden;
    background:
      radial-gradient(circle at 10% 22%, rgba(47,127,224,.75), transparent 45%),
      radial-gradient(circle at 95% 30%, rgba(226,64,94,.55), transparent 30%),
      linear-gradient(180deg, #1d3c9c 0%, #1a2f86 45%, var(--navy-deep) 70%, #1b2575 100%);
    color: var(--white); text-align: center;
  }
  .invitation .fireworks {
    position: absolute; inset: 0 0 auto 0; height: 420px;
    background:
      radial-gradient(circle at 8% 24%, rgba(140,190,255,.45), transparent 28%),
      radial-gradient(circle at 72% 8%, rgba(230,220,160,.18), transparent 22%),
      radial-gradient(circle at 100% 32%, rgba(255,90,110,.45), transparent 22%);
  }
  .invitation .flag {
    position: absolute; left: 0; bottom: 0; width: 592px; height: 290px;
    background:
      linear-gradient(160deg, rgba(70,90,190,.35) 0%, rgba(60,70,170,.15) 40%, transparent 60%),
      radial-gradient(ellipse at 70% 20%, rgba(190,60,90,.35), transparent 45%),
      linear-gradient(180deg, transparent, rgba(40,45,140,.4));
  }
  .invitation .line { position: absolute; left: 0; width: 100%; }
  .title-main { font-family: "Cinzel", serif; font-weight: 700; font-size: 42px; letter-spacing: 2px; line-height: 1; }
  .title-for { font-family: "Open Sans", sans-serif; font-size: 33px; line-height: 1; }
  .brand-name { font-family: "Open Sans", sans-serif; font-weight: 700; font-size: 36px; color: var(--white); line-height: 1; }
  .slogan { font-family: "Open Sans", sans-serif; font-weight: 600; font-size: 32px; line-height: 1; letter-spacing: -.3px; }
  .event-detail { font-family: "Open Sans", sans-serif; font-weight: 700; font-size: 23px; line-height: 1; }
  .venue { font-family: "Open Sans", sans-serif; font-size: 17px; line-height: 1; }
  .rule { position: absolute; left: 148px; width: 296px; height: 1px; background: rgba(217,220,230,.7); }

  /* RSVP card */
  .rsvp {
    position: absolute; left: 644px; top: 415px; width: 528px; height: 369px; overflow: hidden;
    background:
      radial-gradient(circle at 10% 30%, rgba(70,150,240,.8), transparent 35%),
      radial-gradient(circle at 92% 28%, rgba(235,70,100,.75), transparent 30%),
      linear-gradient(100deg, #1f55b8 0%, #2a4aa8 45%, #3c3390 70%, #4a2a78 100%);
    color: var(--white);
  }
  .rsvp .frame { position: absolute; inset: 0; }
  .rsvp .corner { position: absolute; width: 92px; height: 76px; background: rgba(216,201,160,.12); border-radius: 6px; }
  .rsvp-title { position: absolute; top: 26px; left: 0; width: 100%; text-align: center; font-family: "PT Serif", serif; font-weight: 700; font-size: 58px; line-height: 1; }
  .rsvp-name { position: absolute; left: 43px; top: 150px; font-family: "Arimo", sans-serif; font-weight: 700; font-size: 16px; line-height: 1; }
  .rsvp-dots { position: absolute; left: 106px; right: 43px; top: 162px; border-bottom: 2px dotted var(--white); }
  .rsvp-terms { position: absolute; left: 0; width: 100%; top: 221px; text-align: center; font-family: "Arimo", sans-serif; font-size: 16px; letter-spacing: -.3px; line-height: 1; }
  .rsvp-terms strong { font-weight: 700; }
  .rsvp-terms .sep { margin: 0 10px; }
  .rsvp-brand { position: absolute; left: 0; width: 100%; top: 290px; text-align: center; font-family: "Arimo", sans-serif; font-weight: 700; font-size: 17px; line-height: 1; }
</style>
</head>
<body>
<main class="canvas">

  <section class="invitation" aria-label="Holiday party invitation">
    <div class="fireworks" role="img" aria-label="Blue, gold and red fireworks bursting across the night sky"></div>
    <div class="flag" role="img" aria-label="Waving American flag in soft navy and red tones"></div>

    <p class="line title-main" style="top:141px">INVITATION</p>
    <p class="line title-main" style="top:190px">SUITE</p>
    <p class="line title-for" style="top:245px">for</p>
    <p class="line brand-name" style="top:344px">R.L. Penrose Electric</p>
    <p class="line slogan" style="top:469px">Driven by Excellence</p>
    <div class="rule" style="top:534px"></div>
    <p class="line event-detail" style="top:545px">Event: Thursday</p>
    <p class="line event-detail" style="top:579px">Date: Dec 18 2025 | 6-10 PM</p>
    <div class="rule" style="top:620px"></div>
    <p class="line venue" style="top:674px">Ravenna Bellhaven, 318 Quillby Ave, Hammonton NJ 08037</p>
  </section>

  <section class="rsvp" aria-label="RSVP card">
    <div class="corner" style="left:22px;top:22px" role="img" aria-label="Gold filigree corner ornament"></div>
    <div class="corner" style="right:22px;top:22px" role="img" aria-label="Gold filigree corner ornament"></div>
    <div class="corner" style="left:22px;bottom:22px" role="img" aria-label="Gold filigree corner ornament"></div>
    <div class="corner" style="right:22px;bottom:22px" role="img" aria-label="Gold filigree corner ornament"></div>
    <svg class="frame" width="528" height="369" viewBox="0 0 528 369" aria-hidden="true">
      <path d="M10 10 H254 L264 2 L274 10 H518 V176 L526 184 L518 192 V359 H274 L264 367 L254 359 H10 V192 L2 184 L10 176 Z"
            fill="none" stroke="var(--gold-line)" stroke-width="1"/>
    </svg>
    <h2 class="rsvp-title">RSVP</h2>
    <p class="rsvp-name">NAME:</p>
    <div class="rsvp-dots"></div>
    <p class="rsvp-terms"><strong>RSVP BY:</strong> DEC 1<span class="sep">|</span>PLUS ONE ALLOWED.</p>
    <p class="rsvp-brand">R.L. Penrose Electric</p>
  </section>

</main>
</body>
</html>
```